Zielgruppe
Wir sind ein Landwirtschaftsbetrieb für Obstbau und unsere Kunden sind hauptsächlich Privatpersonen und Familien aus der Region sowie Kleinbetriebe wie z. B. regionale Shops.
Aufgabenstellung
Wir benötigen Flaschenetiketten für Fruchtsäfte (3 verschiedene Sorten: Marillennektar, Pfirsichnektar, Kirschennektar) für 0,75 und 0,25 Liter Flaschen und für Schnaps und Liköre (Marillen, Kirschen, Pfirsich, Zwetschke, Kriecherl).
Wir würden eine Vorderseite, die das Design und die Pflichtangaben enthält, bevorzugen.
Die Schrift der Pflichtangaben muss wie folgt ausgeführt werden: Etiketten bis 80 cm2 Kleinbuchstaben mind. 0,9 mm, ab 80 cm2 Kleinbuchstaben mind. 1,2 mm, Großbuchstaben immer mind. 2 mm, das Feld benötigt in etwa 3,5 x 7 cm Platz. Für das Design gibt es noch keine fixe Größe.
Bitte keine Fotos von 'echtem' Obst verwenden.

```html
<!DOCTYPE html>
<html lang="de">
<head>
<meta charset="utf-8">
<title>Obstbau-Lindner – Nektar Etiketten</title>
<link rel="stylesheet" href="https://fonts.googleapis.com/css2?family=Roboto+Condensed:wght@400;700&family=Great+Vibes&family=Pinyon+Script&display=swap">
<style>
  :root {
    --stage: #333333;
    --paper: #ffffff;
    --ink: #111111;
    --marille: #f0812f;
    --kirsche: #b0182c;
    --pfirsich: #e8473f;
    --badge-line: #333333;
  }
  * { box-sizing: border-box; margin: 0; padding: 0; }
  html, body { width: 1200px; height: 859px; overflow: hidden; background: var(--stage); }
  .sheet { position: relative; width: 1200px; height: 859px; }

  .label {
    position: absolute; top: 92px; width: 314px; height: 676px;
    background: var(--paper); font-family: "Roboto Condensed", sans-serif; color: var(--ink);
  }
  .label--marille { left: 104px; --accent: var(--marille); --fruit-a: #fbd38a; --fruit-b: #f39a2e; }
  .label--kirsche { left: 443px; --accent: var(--kirsche); --fruit-a: #e8404a; --fruit-b: #a8121f; }
  .label--pfirsich { left: 782px; --accent: var(--pfirsich); --fruit-a: #fbc86a; --fruit-b: #e0453a; }

  .label__outer-frame {
    position: absolute; inset: 10px; border: 1.5px solid var(--accent);
  }
  .label__corner {
    position: absolute; width: 14px; height: 14px; border-radius: 50%; background: var(--accent);
  }
  .label__corner--tl { left: 8px; top: 8px; }
  .label__corner--tr { right: 8px; top: 8px; }
  .label__corner--bl { left: 8px; bottom: 8px; }
  .label__corner--br { right: 8px; bottom: 8px; }

  .label__inner-frame {
    position: absolute; left: 14px; top: 14px; width: 286px; height: 476px;
    border: 2px solid var(--ink);
  }

  .brand {
    position: absolute; left: 0; right: 0; top: 40px; text-align: center;
    font-weight: 700; font-size: 27px; letter-spacing: 0.5px; color: var(--ink);
  }
  .place {
    position: absolute; left: 0; right: 0; top: 72px; text-align: center;
    font-family: "Pinyon Script", cursive; font-size: 24px; color: var(--ink);
  }
  .fruit-art {
    position: absolute; left: 78px; top: 112px; width: 160px; height: 154px; border-radius: 48%;
    background: radial-gradient(circle at 35% 40%, var(--fruit-a), var(--fruit-b));
  }

  .band {
    position: absolute; left: 10px; top: 276px; width: 294px; height: 118px;
    background: var(--accent); color: var(--paper); text-align: center;
    font-family: "Great Vibes", cursive;
  }
  .band__fruit { display: block; font-size: 54px; line-height: 1; margin-top: 12px; }
  .band__type { display: block; font-size: 36px; line-height: 1; margin-top: 4px; }

  .claim {
    position: absolute; left: 0; right: 0; text-align: center; font-weight: 700; font-size: 12.5px;
  }
  .claim--share { top: 401px; }
  .claim--origin { top: 423px; }

  .seal {
    position: absolute; left: 103px; top: 456px; width: 108px; height: 72px;
    background: var(--paper); border: 1.5px solid var(--badge-line); border-radius: 50%;
    display: flex; align-items: center; justify-content: center; gap: 4px;
    font-weight: 700; font-size: 9.5px; color: var(--ink);
  }
  .seal__dot { width: 8px; height: 8px; border-radius: 50%; background: var(--ink); }

  .volume {
    position: absolute; left: 224px; top: 458px; font-size: 20px; color: var(--accent);
  }
  .volume__mark { color: var(--ink); }

  .facts {
    position: absolute; left: 18px; right: 18px; top: 534px; text-align: center;
    font-size: 11.6px; line-height: 15.8px;
  }
  .facts strong { font-weight: 700; }

  .footer-bar {
    position: absolute; left: 58px; top: 634px; width: 198px; height: 19px;
    background: var(--accent); color: var(--paper); text-align: center;
    font-weight: 700; font-size: 12px; line-height: 19px;
  }
</style>
</head>
<body>
<main class="sheet">

  <article class="label label--marille">
    <div class="label__outer-frame"></div>
    <span class="label__corner label__corner--tl"></span><span class="label__corner label__corner--tr"></span>
    <span class="label__corner label__corner--bl"></span><span class="label__corner label__corner--br"></span>
    <div class="label__inner-frame"></div>
    <p class="brand">OBSTBAU-LINDNER</p>
    <p class="place">Weidenau</p>
    <div class="fruit-art" role="img" aria-label="Illustration: Marillen mit Blättern, eine halbierte Marille"></div>
    <h2 class="band"><span class="band__fruit">Marillen</span><span class="band__type">Nektar</span></h2>
    <p class="claim claim--share">Fruchanteil mindestens 40 %</p>
    <p class="claim claim--origin">Marillen aus einiger Production</p>
    <div class="seal"><span class="seal__dot"></span>OBSTBAU-LINDNER</div>
    <p class="volume"><span class="volume__mark">e</span>0,75L</p>
    <div class="facts">
      <p>Josef Lindner, Am Anger 14 &nbsp;•&nbsp; A - 2234 Weidenau.</p>
      <p><strong>Zutaten:</strong> Marillenmark (mind. 40 %), Wasser, Zucker</p>
      <p>Ohne Konservierungsstoffe &amp; künstliche Aromen</p>
      <p>Nach dem Öffnen gekühlt lagern und innerhalb</p>
      <p>von 3 Tagen verbrauchen.</p>
      <p>Vor Gebrauch gut schütteln.</p>
    </div>
    <p class="footer-bar">Marillen aus einiger Production</p>
  </article>

  <article class="label label--kirsche">
    <div class="label__outer-frame"></div>
    <span class="label__corner label__corner--tl"></span><span class="label__corner label__corner--tr"></span>
    <span class="label__corner label__corner--bl"></span><span class="label__corner label__corner--br"></span>
    <div class="label__inner-frame"></div>
    <p class="brand">OBSTBAU-LINDNER</p>
    <p class="place">Weidenau</p>
    <div class="fruit-art" role="img" aria-label="Illustration: rote Kirschen mit Stielen"></div>
    <h2 class="band"><span class="band__fruit">Kirschen</span><span class="band__type">Nektar</span></h2>
    <p class="claim claim--share">Fruchanteil mindestens 40 %</p>
    <p class="claim claim--origin">Marillen aus einiger Production</p>
    <div class="seal"><span class="seal__dot"></span>OBSTBAU-LINDNER</div>
    <p class="volume"><span class="volume__mark">e</span>0,75L</p>
    <div class="facts">
      <p>Josef Lindner, Am Anger 14 &nbsp;•&nbsp; A - 2234 Weidenau.</p>
      <p><strong>Zutaten:</strong> Marillenmark (mind. 40 %), Wasser, Zucker</p>
      <p>Ohne Konservierungsstoffe &amp; künstliche Aromen.</p>
      <p>Nach dem Öffnen gekühlt lagern und innerhalb</p>
      <p>von 3 Tagen verbrauchen.</p>
      <p>Vor Gebrauch gut schütteln.</p>
    </div>
    <p class="footer-bar">Marillen aus einiger Production</p>
  </article>

  <article class="label label--pfirsich">
    <div class="label__outer-frame"></div>
    <span class="label__corner label__corner--tl"></span><span class="label__corner label__corner--tr"></span>
    <span class="label__corner label__corner--bl"></span><span class="label__corner label__corner--br"></span>
    <div class="label__inner-frame"></div>
    <p class="brand">OBSTBAU-LINDNER</p>
    <p class="place">Weidenau</p>
    <div class="fruit-art" role="img" aria-label="Illustration: Pfirsich mit Blättern, ein halbierter Pfirsich mit Kern"></div>
    <h2 class="band"><span class="band__fruit">Pfirsich</span><span class="band__type">Nektar</span></h2>
    <p class="claim claim--share">Fruchanteil mindestens 40 %</p>
    <p class="claim claim--origin">Marillen aus einiger Production</p>
    <div class="seal"><span class="seal__dot"></span>OBSTBAU-LINDNER</div>
    <p class="volume"><span class="volume__mark">e</span>0,75L</p>
    <div class="facts">
      <p>Josef Lindner, Am Anger 14 &nbsp;•&nbsp; A - 2234 Weidenau.</p>
      <p><strong>Zutaten:</strong> Marillenmark (mind. 40 %), Wasser, Zucker</p>
      <p>Ohne Konservierungsstoffe &amp; künstliche Aromen.</p>
      <p>Nach dem Öffnen gekühlt lagern und innerhalb</p>
      <p>von 3 Tagen verbrauchen.</p>
      <p>Vor Gebrauch gut schütteln.</p>
    </div>
    <p class="footer-bar">Marillen aus einiger Production</p>
  </article>

</main>
</body>
</html>
```